Design a leading edge business card for an architectural company

We believe that Velistra Design Collective is redefining the architectural industry. With that, we need a leading edge business card for the company that focuses on landscape architecture, design, and construction.

Our clients are businesses and homeowners so we need a clean, simple, and professional-looking logo. But we want something special. Design must be elegant but unexpected.

Color preferences:
- Preferably with black background but not a must
- Text should be light colored
- Overall, don’t use too much colors.

Content:
- Front of card must contain either just the logo or the logo and business name only.
- Back of card will show the other information (name, title, phone number, email, website, location).

Style:
- Maybe embossing, de-bossing, or spot UV
- Layout should be landscape unless you prove us otherwise.

Size: 1050 x 600 pixels (with 1/8th inch bleed: 1125 x 675 pixels)

Attached is the company logo to incorporate in the design.

```html
<!DOCTYPE html>
<html lang="en">
<head>
<meta charset="utf-8">
<title>Velistra Design Collective – Business Card</title>
<link href="https://fonts.googleapis.com/css2?family=Lato:ital,wght@0,400;0,700;1,400&display=swap" rel="stylesheet">
<style>
  :root {
    --stage: #000000;
    --brand-blue: #1f5a9e;
    --brand-blue-light: #4f86c6;
    --card-white: #ffffff;
    --ink: #3a3f47;
  }
  * { margin: 0; padding: 0; box-sizing: border-box; }
  html, body {
    width: 1200px; height: 675px; overflow: hidden;
    background: var(--stage);
    font-family: "Lato", Arial, sans-serif;
  }
  .stage { position: relative; width: 1200px; height: 675px; }
  .card {
    position: absolute; top: 183px;
    width: 540px; height: 309px;
    overflow: hidden;
  }
  /* Contact side */
  .card--contact { left: 40px; background: var(--card-white); }
  .card__swoosh { position: absolute; inset: 0; }
  .brand-name {
    position: absolute; left: 112px; top: 92px;
    display: flex; align-items: center; gap: 10px;
  }
  .brand-name__dot {
    width: 12px; height: 12px; border-radius: 50%;
    background: var(--brand-blue); flex: none;
  }
  .brand-name__text {
    font-weight: 700; font-size: 18px; line-height: 1.25;
    letter-spacing: 2px; text-transform: uppercase;
    color: var(--brand-blue);
  }
  .person { position: absolute; left: 300px; top: 62px; }
  .person__name { font-size: 17px; color: var(--ink); }
  .person__title { font-size: 11px; color: var(--brand-blue); margin-top: 3px; }
  .contact-list {
    position: absolute; left: 282px; top: 160px;
    list-style: none;
  }
  .contact-list li {
    display: flex; align-items: center; gap: 8px;
    font-size: 11px; color: var(--ink); line-height: 1.5;
  }
  .contact-list svg { width: 11px; height: 11px; fill: var(--brand-blue); flex: none; }
  .contact-list .address { align-items: flex-start; }
  .contact-list .address svg { margin-top: 3px; }

  /* Brand side */
  .card--brand { left: 620px; background: var(--brand-blue); color: var(--card-white); }
  .brand-center {
    position: absolute; left: 0; right: 0; top: 118px;
    display: flex; justify-content: center; align-items: center; gap: 12px;
  }
  .brand-center__dot {
    width: 14px; height: 14px; border-radius: 50%;
    background: var(--card-white);
  }
  .brand-center__text {
    font-weight: 700; font-size: 24px; letter-spacing: 3px;
    text-transform: uppercase; color: var(--card-white);
  }
  .brand-web {
    position: absolute; left: 34px; bottom: 40px;
    font-size: 11px; letter-spacing: .3px; color: var(--card-white);
  }
</style>
</head>
<body>
<main class="stage">

  <section class="card card--contact">
    <svg class="card__swoosh" viewBox="0 0 540 309" preserveAspectRatio="none" aria-hidden="true">
      <path d="M0 0 H150 Q40 110 72 309 H0 Z" fill="var(--brand-blue)"/>
      <path d="M160 0 Q50 110 82 309" fill="none" stroke="var(--brand-blue-light)" stroke-width="3"/>
    </svg>

    <div class="brand-name">
      <span class="brand-name__dot"></span>
      <span class="brand-name__text">Velistra<br>Design Collective</span>
    </div>

    <div class="person">
      <p class="person__name">Jordan Ellery</p>
      <p class="person__title">Managing Director</p>
    </div>

    <ul class="contact-list">
      <li class="address">
        <svg viewBox="0 0 12 12"><path d="M6 1 L11 5.5 H9.5 V11 H2.5 V5.5 H1 Z"/></svg>
        <span>Unit 48, Harrow Lane,<br>Brookfield 4821, Country</span>
      </li>
      <li>
        <svg viewBox="0 0 12 12"><path d="M2.5 1 L4.5 1 L5.5 3.5 L4.2 4.6 Q5.2 6.8 7.4 7.8 L8.5 6.5 L11 7.5 L11 9.5 Q10.5 11 9 11 Q1 10 1 3 Q1 1.5 2.5 1 Z"/></svg>
        <span>(555) 214-3870</span>
      </li>
      <li>
        <svg viewBox="0 0 12 12"><path d="M1 3 H11 V10 H1 Z M2 4 V5 L6 7.5 L10 5 V4 L6 6.5 Z" fill-rule="evenodd"/></svg>
        <span>(555) 214-3871</span>
      </li>
      <li>
        <svg viewBox="0 0 12 12"><path d="M1 2.5 H11 V9.5 H1 Z M1.8 3.3 L6 6.4 L10.2 3.3" stroke="#fff" stroke-width=".8"/></svg>
        <span>info@velistradesign.com</span>
      </li>
      <li>
        <svg viewBox="0 0 12 12"><circle cx="6" cy="6" r="5"/><path d="M1 6 H11 M6 1 Q3 6 6 11 M6 1 Q9 6 6 11" fill="none" stroke="#fff" stroke-width=".7"/></svg>
        <span>www.velistradesign.com</span>
      </li>
    </ul>
  </section>

  <section class="card card--brand">
    <div class="brand-center">
      <span class="brand-center__dot"></span>
      <span class="brand-center__text">Velistra Design Collective</span>
    </div>
    <p class="brand-web">www.velistradesigncollective.com</p>
  </section>

</main>
</body>
</html>
```